Standard logo business card

We are seeking a solid, somewhat understated professional design. We are a tech company. We like fonts similar to Aptifer Slab. Front side will be white with the contact information and a small version of our primary (Light background) logo.

(We have three people so we will have three names and titles)

Back side will hold our reverse logo on dark background along with the tagline:

"Intelligent annotation solutions for complex data"

Target Market(s)

Professionals, Tech

Industry/Entity Type

Business

Contact Information for Business Card

Name
Title

Phone
Email
City, State
Website

[We will email leading designer specific contact information)

Font styles to use
Serif

Requirements
Must have
• Colors are:
• Orange RGB 245,92,23
• Blue RGB 3,34,56
Nice to have
• We like a split with the Name and Title on the right and then contact details (below) on the left.

```html
<!DOCTYPE html>
<html lang="en">
<head>
<meta charset="utf-8">
<title>Norvana business card</title>
<link rel="stylesheet" href="https://fonts.googleapis.com/css2?family=Arimo:wght@400;700&display=swap">
<style>
  :root {
    --backdrop: #62241f;
    --paper: #fdfcfa;
    --ink: #26272b;
    --night: #26272b;
    --orange: #e85d26;
    --white: #ffffff;
  }
  * { margin: 0; padding: 0; box-sizing: border-box; }
  html, body { width: 1200px; height: 951px; overflow: hidden; }
  body { background: var(--backdrop); position: relative; font-family: "Arimo", Arial, sans-serif; }

  .card { position: absolute; top: 37px; width: 527px; height: 877px; overflow: hidden; }
  .card--front { left: 45px; background: var(--paper); }
  .card--back { left: 634px; background: var(--night); }

  .turned {
    position: absolute;
    transform: translate(-50%, -50%) rotate(-90deg);
    white-space: nowrap;
  }

  .wordmark {
    font-family: "Arimo", Arial, sans-serif;
    font-weight: 700;
    line-height: 1;
    text-align: center;
  }
  .wordmark--front { left: 190px; top: 188px; width: 330px; font-size: 78px; color: var(--ink); }
  .wordmark--back { left: 262px; top: 367px; width: 540px; font-size: 132px; color: var(--white); }

  .mark-square { position: absolute; background: var(--orange); border-radius: 3px; }
  .mark-square--front { left: 154px; top: 366px; width: 78px; height: 78px; }
  .mark-square--back { left: 198px; top: 645px; width: 120px; height: 120px; }

  .person { left: 323px; top: 222px; width: 262px; color: var(--ink); }
  .person__name { font-weight: 700; font-size: 30px; letter-spacing: 0.5px; line-height: 40px; }
  .person__title { font-size: 23px; line-height: 30px; }

  .contact {
    left: 258px; top: 684px; width: 240px;
    text-align: center; color: var(--ink);
    font-size: 20px; line-height: 32px; letter-spacing: 0.5px;
    font-style: normal;
  }

  .tagline {
    left: 335px; top: 370px; width: 522px;
    color: var(--white); font-size: 19px; letter-spacing: 0.6px;
    line-height: 26px; text-align: center;
    border-bottom: 2px solid var(--white);
  }
</style>
</head>
<body>
  <section class="card card--front">
    <div class="turned wordmark wordmark--front">norvana</div>
    <div class="mark-square mark-square--front"></div>
    <div class="turned person">
      <p class="person__name">DANIEL OTIENO</p>
      <p class="person__title">Technician</p>
    </div>
    <address class="turned contact">
      +00 9800 5521<br>
      Nairobi<br>
      daniel@norvana.com<br>
      www.norvana.com
    </address>
  </section>

  <section class="card card--back">
    <div class="turned wordmark wordmark--back">norvana</div>
    <p class="turned tagline">Intelligent annotation solutions for complex data</p>
    <div class="mark-square mark-square--back"></div>
  </section>
</body>
</html>
```